Business Card for bespoke luxury cupcakes and cakes
childrens parties, baby showers, seasonal designs, christenings, 3D and 2D designs
Bright & Fun-filled
Tumble Bakes Ltd
London
morvenaltoski@mailnest.co.uk
www.pagelink.co.uk/TumbleBakesLtd

```html
<!DOCTYPE html>
<html lang="en">
<head>
<meta charset="utf-8">
<title>Tumble Bakes Ltd – Business Card</title>
<link rel="stylesheet" href="https://fonts.googleapis.com/css2?family=Quicksand:wght@400;500;700&display=swap">
<style>
  :root {
    --stage: #d9d9d9;
    --magenta: #c2185b;
    --magenta-light: #e04c8a;
    --magenta-deep: #8e0e42;
    --cocoa: #4a423a;
    --cocoa-light: #6e655a;
    --cocoa-deep: #2f2a25;
    --cream: #efe9d4;
    --ink: #3a322b;
    --white: #ffffff;
    --photo-a: #d9cfc4;
    --photo-b: #b9b39a;
    --photo-c: #e7d3d6;
  }
  * { box-sizing: border-box; margin: 0; padding: 0; }
  html, body { width: 1200px; height: 898px; overflow: hidden; }
  body {
    background: var(--stage);
    font-family: "Quicksand", sans-serif;
    display: flex;
    flex-direction: column;
    align-items: center;
    justify-content: center;
    gap: 40px;
  }
  .card {
    position: relative;
    width: 660px;
    height: 377px;
    border-radius: 18px;
    overflow: hidden;
  }
  .card-backdrop { position: absolute; inset: 0; }
  .card-back .card-backdrop {
    background: radial-gradient(circle at 50% 20%, var(--magenta-light), var(--magenta) 55%, var(--magenta-deep));
  }
  .card-front .card-backdrop {
    background: radial-gradient(circle at 50% 18%, var(--cocoa-light), var(--cocoa) 55%, var(--cocoa-deep));
  }
  .brand {
    position: absolute;
    left: 0; right: 0;
    display: flex;
    justify-content: center;
    align-items: center;
    gap: 10px;
    font-weight: 700;
    font-size: 34px;
    line-height: 1;
    letter-spacing: 0.5px;
  }
  .brand-dot { width: 22px; height: 22px; border-radius: 50%; }
  .card-back .brand { top: 26px; color: var(--white); }
  .card-back .brand-dot { background: var(--white); }
  .card-front .brand { top: 42px; color: var(--magenta-light); }
  .card-front .brand-dot { background: var(--magenta-light); }

  .label-band {
    position: absolute;
    display: flex;
    align-items: center;
    justify-content: center;
    background: var(--cream);
    color: var(--ink);
    line-height: 1;
  }
  .company-band {
    left: 228px; width: 204px;
    top: 74px; height: 28px;
    font-size: 16px; font-weight: 700;
  }

  .photo-strip {
    position: absolute;
    left: 0; right: 0;
    top: 120px;
    height: 152px;
    background: rgba(255,255,255,0.92);
    display: flex;
    justify-content: center;
    gap: 8px;
    padding: 10px 0;
  }
  .photo { width: 196px; height: 132px; }
  .photo-1 { background: linear-gradient(160deg, #efe8e2, var(--photo-a)); }
  .photo-2 { background: linear-gradient(160deg, #c9c4ad, var(--photo-b) 60%, #8f9a6a); }
  .photo-3 { background: linear-gradient(160deg, #f4e8ea, var(--photo-c)); }

  .back-url {
    position: absolute;
    right: 28px;
    bottom: 46px;
    color: var(--white);
    font-weight: 500;
    font-size: 17px;
    letter-spacing: 0.3px;
  }

  .tagline {
    position: absolute;
    left: 0; right: 0;
    top: 120px;
    text-align: center;
    color: var(--white);
    font-weight: 400;
    font-size: 25px;
    line-height: 1.3;
  }
  .wave-band { position: absolute; left: 0; bottom: 0; }
  .url-band {
    left: 116px; width: 428px;
    top: 269px; height: 40px;
    font-size: 19px; font-weight: 500;
  }
  .contact-line {
    position: absolute;
    left: 28px; right: 28px;
    bottom: 14px;
    display: flex;
    justify-content: space-between;
    color: var(--white);
    font-size: 14px;
    font-weight: 500;
  }
  .contact-label { margin-right: 10px; opacity: 0.9; }
</style>
</head>
<body>

  <section class="card card-back" aria-label="Business card reverse">
    <div class="card-backdrop" role="img" aria-label="Magenta radiating background pattern"></div>
    <div class="brand"><span class="brand-dot"></span>Tumble Bakes</div>
    <div class="label-band company-band">Tumble Bakes Ltd</div>
    <div class="photo-strip">
      <div class="photo photo-1" role="img" aria-label="Photo of a white two-tier celebration cake with colourful toy figures"></div>
      <div class="photo photo-2" role="img" aria-label="Photo of a green themed celebration cake with figures on top"></div>
      <div class="photo photo-3" role="img" aria-label="Photo of a pink christening cake with a bow"></div>
    </div>
    <div class="back-url">www.pagelink.co.uk/TumbleBakesLtd</div>
  </section>

  <section class="card card-front" aria-label="Business card front">
    <div class="card-backdrop" role="img" aria-label="Brown radiating background pattern"></div>
    <div class="brand"><span class="brand-dot"></span>Tumble Bakes</div>
    <p class="tagline">Bespoke cupcakes and cake designs<br>for any occasion</p>
    <svg class="wave-band" width="660" height="140" viewBox="0 0 660 140" aria-hidden="true">
      <path d="M0,40 C160,10 300,30 420,22 C520,16 600,10 660,0 L660,140 L0,140 Z" fill="var(--magenta-deep)"/>
      <path d="M0,52 C160,22 300,40 420,32 C520,26 600,20 660,12 L660,140 L0,140 Z" fill="var(--magenta)"/>
    </svg>
    <div class="label-band url-band">www.pagelink.co.uk/TumbleBakesLtd</div>
    <div class="contact-line">
      <span><span class="contact-label">Phone</span>+44 7700 900 418</span>
      <span><span class="contact-label">Email</span>morvenaltoski@mailnest.co.uk</span>
    </div>
  </section>

</body>
</html>
```